DESIGN OF STATIONERY - TALVORA MED

WE WORK IN THE FIELD OF HEALTH (IMAGING: MRI - CT ETC.).
WE WOULD LIKE TO CREATE THE ENTIRE STATIONERY DESIGN : LETTERHEAD, BUSINESS CARD, CALENDAR, INVOICES, CD HOLDER, ETC.

Target Market(s)

PERSONS UNDERTAKING HEALTH EXAMINATIONS

```html
<!DOCTYPE html>
<html lang="en">
<head>
<meta charset="utf-8">
<title>Talvora Med – Letterhead</title>
<link href="https://fonts.googleapis.com/css2?family=Open+Sans:wght@400;600&family=Roboto:wght@400&display=swap" rel="stylesheet">
<style>
  :root {
    --backdrop: #dcdcdc;
    --paper: #f7f7f7;
    --ink: #4a4a4a;
    --brand-blue: #1a6fb5;
    --brand-teal: #16a096;
    --footer-ink: #5a5a5a;
  }
  * { box-sizing: border-box; margin: 0; padding: 0; }
  html, body {
    width: 1153px; height: 1200px; overflow: hidden;
    background: var(--backdrop);
  }
  .letterhead {
    position: absolute;
    left: 182px; top: 50px;
    width: 788px; height: 1100px;
    background: var(--paper);
    box-shadow: 0 10px 30px rgba(0,0,0,0.12);
    font-family: "Open Sans", sans-serif;
    color: var(--ink);
  }
  .brand {
    position: absolute; left: 71px; top: 58px;
    display: flex; align-items: center; gap: 12px;
  }
  .brand-dot {
    width: 22px; height: 22px; border-radius: 50%;
    background: var(--brand-blue);
  }
  .brand-name {
    font-family: "Open Sans", sans-serif;
    font-weight: 600; font-size: 40px; line-height: 1;
    color: var(--brand-blue); letter-spacing: -0.5px;
  }
  .brand-tagline {
    position: absolute; left: 73px; top: 110px;
    font-size: 13px; color: var(--brand-teal); letter-spacing: 0.3px;
  }
  .letter-body {
    position: absolute; left: 71px; top: 256px; width: 644px;
    font-size: 14.6px; line-height: 21.2px;
  }
  .letter-body p { margin-bottom: 21px; text-align: justify; }
  .letter-body .salutation, .letter-body .closing { text-align: left; }
  .signature {
    position: absolute; left: 71px; top: 856px;
    width: 92px; height: 86px;
    background: linear-gradient(135deg, #ececec, #e2e2e2);
    border-radius: 4px;
  }
  .contact-footer {
    position: absolute; left: 0; right: 0; top: 1016px;
    text-align: center;
    font-family: "Roboto", sans-serif; font-size: 15.6px; line-height: 24px;
    color: var(--footer-ink);
  }
  .contact-footer .label { color: var(--brand-blue); }
  .contact-footer .item { margin: 0 4px; }
</style>
</head>
<body>
  <main class="letterhead">
    <header>
      <div class="brand">
        <span class="brand-dot"></span>
        <span class="brand-name">Talvora Med</span>
      </div>
      <div class="brand-tagline">Health Care Diagnostic</div>
    </header>

    <section class="letter-body">
      <p class="salutation">Dear customer,</p>
      <p>Lorem ipsum dolor sit amet, consectetur adipisicing elit, sed do eiusmod tempor incididunt ut labore et dolore magna aliqua. Ut enim ad minim veniam, quis nostrud exercitation ullamco laboris nisi ut aliquip ex ea commodo consequat. Duis aute irure dolor in reprehenderit in voluptate velit esse cillum dolore eu fugiat nulla pariatur. Excepteur sint occaecat cupidatat non proident, sunt in culpa qui officia deserunt mollit anim id est laborum.</p>
      <p>Lorem ipsum dolor sit amet, consectetur adipisicing elit, sed do eiusmod tempor incididunt ut labore et dolore magna aliqua. Ut enim ad minim veniam, quis nostrud exercitation ullamco laboris nisi ut aliquip ex ea commodo consequat. Duis aute irure dolor in reprehenderit in voluptate velit esse cillum dolore eu fugiat nulla pariatur. Excepteur sint occaecat cupidatat non proident, sunt in culpa qui officia deserunt mollit anim id est laborum.</p>
      <p>Lorem ipsum dolor sit amet, consectetur adipisicing elit, sed do eiusmod tempor incididunt ut labore et dolore magna aliqua. Ut enim ad minim veniam, quis nostrud exercitation ullamco laboris nisi ut aliquip ex ea commodo consequat. Duis aute irure dolor in reprehenderit in voluptate velit esse cillum dolore eu fugiat nulla pariatur. Excepteur sint occaecat cupidatat non proident, sunt in culpa qui officia deserunt mollit anim id est laborum.</p>
      <p>Lorem ipsum dolor sit amet, consectetur adipisicing elit, sed do eiusmod tempor incididunt ut labore et dolore magna aliqua. Ut enim ad minim veniam, quis nostrud exercitation ullamco laboris nisi ut aliquip ex ea commodo consequat. Duis aute irure dolor in reprehenderit.</p>
      <p class="closing">Yours Sincerely,</p>
    </section>

    <div class="signature" role="img" aria-label="Handwritten signature of the sender"></div>

    <footer class="contact-footer">
      <div>Corven Court, 18 Ashby Lane, London SE4 7QT</div>
      <div>
        <span class="item"><span class="label">P :</span> 0208 555 0147</span>
        <span class="item"><span class="label">E :</span> info@talvoramed.com</span>
        <span class="item"><span class="label">W :</span> www.talvoramed.com</span>
      </div>
    </footer>
  </main>
</body>
</html>
```